Business Card Designs

Looking to design a 3.5" x 2" standard business card for our employees.
The design needs to be sleek, simple, and modern. We would like our logo (attached) to be incorporated, but not in that colour, rather an outline of the logo in either gold or silver (whichever looks better).

Modern and Simple is what we are looking for, but be creative in incorporating the logo.

```html
<!DOCTYPE html>
<html lang="en">
<head>
<meta charset="utf-8">
<title>Harbourline Residences – Business Card</title>
<link rel="stylesheet" href="https://fonts.googleapis.com/css2?family=Lato:wght@300;400;700&display=swap">
<style>
  :root {
    --backdrop: #8e8e8e;
    --card: #262626;
    --ink-muted: #8f8f8f;
    --ink-soft: #a5a5a5;
    --ink-light: #d2d2d2;
    --rule: #6a6a6a;
    --mark: #9c9c9c;
  }
  * { margin: 0; padding: 0; box-sizing: border-box; }
  html, body {
    width: 1200px; height: 1200px; overflow: hidden;
    background: var(--backdrop);
    font-family: "Lato", sans-serif;
  }
  .canvas { position: relative; width: 1200px; height: 1200px; }
  .card {
    position: absolute; left: 281px; width: 641px; height: 366px;
    background: var(--card); border-radius: 18px;
  }
  .card--front { top: 195px; }
  .card--back { top: 639px; }

  .brand-corner {
    position: absolute; right: 42px; top: 44px;
    display: flex; align-items: center; gap: 10px;
  }
  .brand-square { width: 16px; height: 16px; background: var(--mark); }
  .brand-name {
    color: var(--mark); font-weight: 700; font-size: 18px;
    letter-spacing: 2px; text-transform: uppercase; line-height: 1.3; text-align: right;
  }

  .person { position: absolute; left: 39px; top: 180px; }
  .person-name {
    color: var(--ink-muted); font-size: 26px; font-weight: 400;
    letter-spacing: 0.5px; text-transform: uppercase; line-height: 1;
  }
  .person-role { color: var(--ink-soft); font-size: 18px; margin-top: 9px; }

  .divider {
    position: absolute; left: 39px; right: 42px; top: 247px;
    height: 1px; background: var(--rule);
  }

  .contacts { position: absolute; left: 39px; top: 262px; list-style: none; }
  .contacts li {
    display: flex; align-items: center; gap: 9px;
    color: var(--ink-light); font-size: 15.5px; height: 22.5px; letter-spacing: 0.3px;
  }
  .contacts svg { width: 13px; height: 13px; fill: none; stroke: var(--ink-muted); stroke-width: 1.4; }

  .address {
    position: absolute; right: 42px; top: 262px; text-align: right; font-style: normal;
  }
  .address span { display: block; font-size: 15.5px; height: 22.5px; line-height: 22.5px; color: var(--ink-light); letter-spacing: 0.3px; }
  .address .address-company { color: var(--ink-muted); font-weight: 300; }

  .back-brand {
    position: absolute; left: 0; right: 0; top: 140px;
    display: flex; flex-direction: column; align-items: center; gap: 16px;
  }
  .back-brand .brand-square { width: 22px; height: 22px; }
  .back-brand .brand-name { font-size: 24px; letter-spacing: 4px; text-align: center; }
</style>
</head>
<body>
<main class="canvas">
  <section class="card card--front" aria-label="Business card front">
    <div class="brand-corner">
      <span class="brand-name">Harbourline</span>
      <span class="brand-square"></span>
    </div>

    <div class="person">
      <h1 class="person-name">Daniel Reyes</h1>
      <p class="person-role">Founder &amp; CEO</p>
    </div>

    <div class="divider"></div>

    <ul class="contacts">
      <li>
        <svg viewBox="0 0 14 14"><rect x="3.5" y="1" width="7" height="12" rx="1.2"/><line x1="6" y1="11" x2="8" y2="11"/></svg>
        (123) 456-7890
      </li>
      <li>
        <svg viewBox="0 0 14 14"><rect x="1" y="3" width="12" height="8.5"/><polyline points="1,3 7,8 13,3"/></svg>
        hello@yourwebsite.com
      </li>
      <li>
        <svg viewBox="0 0 14 14"><circle cx="7" cy="7" r="5.8"/><ellipse cx="7" cy="7" rx="2.5" ry="5.8"/><line x1="1.2" y1="7" x2="12.8" y2="7"/></svg>
        www.yourwebsite.com
      </li>
    </ul>

    <address class="address">
      <span class="address-company">Harbourline Residences</span>
      <span>123 Anywhere St</span>
      <span>Any City, State 12345</span>
    </address>
  </section>

  <section class="card card--back" aria-label="Business card back">
    <div class="back-brand">
      <span class="brand-square"></span>
      <span class="brand-name">Harbourline<br>Residences</span>
    </div>
  </section>
</main>
</body>
</html>
```